Business Card Design

Marla Quibbet
Artist of Contemporary/Modern/Representational Art
Contact: 0457219308
Please include my web site (thanks)! http://www.artvault913.com.au/marla-quibbet
And
Email: marlaquibbet@fernpost.example

Target Market(s)

Modern professional People who know what they like in modern contemporary art and have the means to purchase it.

Industry/Entity Type

Business

Contact Information for Business Card

Marla Quibbet
Contact: 0457219308

Font styles to use
Sans Serif

Requirements
Must have
• Simplicity & to the point
Keep the font modern/ contemporary
Nice to have
• A portrait of me and one piece of work on the business card (one on each side).
Should not have
• I'm not into butterflies.
No feminine style swirls
Nor I like swirls that look like tatoos

```html
<!DOCTYPE html>
<html lang="en">
<head>
<meta charset="utf-8">
<title>Marla Quibbet – Business Card</title>
<link href="https://fonts.googleapis.com/css2?family=Michroma&family=Montserrat:wght@400;500&display=swap" rel="stylesheet">
<style>
  :root {
    --page-bg: #e9e6e1;
    --card-black: #000000;
    --ink-white: #ffffff;
    --portrait-light: #d8d8d8;
    --portrait-dark: #5a5a5a;
    --art-sky: #7fc3d6;
    --art-river: #2f7fa6;
    --art-green: #4f9a3c;
    --art-city: #9a9aa4;
  }
  html, body {
    margin: 0;
    padding: 0;
    width: 1200px;
    height: 1023px;
    overflow: hidden;
    background: var(--page-bg);
  }
  .canvas {
    position: relative;
    width: 1200px;
    height: 1023px;
  }
  .card {
    position: absolute;
    left: 220px;
    width: 760px;
    height: 434px;
    overflow: hidden;
    box-shadow: 0 6px 18px rgba(0,0,0,0.18);
  }
  .card--front {
    top: 52px;
    background: var(--card-black);
    color: var(--ink-white);
  }
  .card--back {
    top: 536px;
  }
  .portrait {
    position: absolute;
    left: 52px;
    top: 170px;
    width: 236px;
    height: 214px;
    background: linear-gradient(160deg, var(--portrait-light) 0%, #a9a9a9 45%, var(--portrait-dark) 100%);
  }
  .details {
    position: absolute;
    left: 312px;
    top: 160px;
    width: 420px;
  }
  .name {
    font-family: "Michroma", sans-serif;
    font-size: 27px;
    font-weight: 400;
    letter-spacing: 0.2em;
    text-transform: uppercase;
    margin: 0;
    line-height: 1.2;
    white-space: nowrap;
  }
  .rule {
    height: 3px;
    background: var(--ink-white);
    border: 0;
    margin: 12px 0;
  }
  .tagline {
    font-family: "Montserrat", sans-serif;
    font-size: 15px;
    margin: 0;
    white-space: nowrap;
  }
  .contact {
    font-family: "Montserrat", sans-serif;
    font-size: 15px;
    letter-spacing: 0.05em;
    margin: 0 0 8px;
    white-space: nowrap;
  }
  .artwork {
    width: 100%;
    height: 100%;
    display: block;
  }
</style>
</head>
<body>
<main class="canvas">
  <section class="card card--front">
    <div class="portrait" role="img" aria-label="Black and white portrait photograph of the artist"></div>
    <div class="details">
      <h1 class="name">Marla Quibbet</h1>
      <hr class="rule">
      <p class="tagline">Artist of Contemporary | Modern | Representational Art</p>
      <hr class="rule">
      <p class="contact">0457219308 | marlaquibbet@fernpost.example</p>
      <p class="contact">www.artvault913.com.au/marla-quibbet</p>
    </div>
  </section>

  <section class="card card--back">
    <svg class="artwork" viewBox="0 0 760 434" role="img" aria-label="Colourful illustrated aerial view of a city with a river, parks and stadiums">
      <defs>
        <linearGradient id="artTones" x1="0" y1="0" x2="1" y2="1">
          <stop offset="0" stop-color="var(--art-city)"/>
          <stop offset="0.35" stop-color="var(--art-green)"/>
          <stop offset="0.6" stop-color="var(--art-river)"/>
          <stop offset="1" stop-color="var(--art-sky)"/>
        </linearGradient>
      </defs>
      <rect width="760" height="434" fill="url(#artTones)"/>
    </svg>
  </section>
</main>
</body>
</html>
```